Complete redesign of site for leading equipment supplier and service company

Looking for a new website design to portray our offerings for customers. Bay & Gate is a distributor, installer and service provider for loading dock equipment and industrial doors. We are a factory authorized dealer for a number of top brand names and also provide service after the sale on our equipment as well as competitors equipment. We are also in the midst of developing a service program tied to a QR coding system that would need to be incorporated in the website where a customer can scan a QR code and be brought to a specific "Service Request" portal that would be a form they could fill out to send to our service department.
Site should also feature product information pages for our base of product offerings, a completed projects area where we can showcase the work we've done, and a bio area for our sales and management team.

Some information for research:

Our Products That We Sell:

morrowliftworks.com
pallanraisetech.com
vqxgates.com
nhlsupplies.com
https://www.garvin-holtby.com/commercial-doors
https://www.pelmagates.com/
https://www.ulogates.com/

Similar Companies and Competitors:

http://www.quaddelmachinery.com/
https://www.easternbaysupplies.com/
https://www.moonmachinery.com/
https://www.ravenhollis.com/
https://pelvo.quandrift.com/en/us?gclid=ZqmPLRtyuv5XNCCFkpOmQD_ZYKJT0sVUr8PWHnm3K7Pxa3ZQ-PxluzkMnb-opiIIDmRtxu4BzJpTfLh9rmzDGbnwQ_ExcEB

Target Market(s)

Existing and potential customers throughout the greater New England region including:
Manufacturing
Distribution
Cold Storage
Pharmaceutical
Food Production
Beverage Bottling
Warehousing

Coding

Coded - Design and coding required

Number of Pages Required

5+ page

Colors
9ccb3b
ecf7fb

Requirements
Must have
• Home Page
Product Page
Service Page
Contact Page
Separate page that will be directed to from a QR code that we will supply to specific customers

```html
<!DOCTYPE html>
<html lang="en">
<head>
<meta charset="utf-8">
<title>Bay &amp; Gate New England</title>
<link href="https://fonts.googleapis.com/css2?family=Montserrat:wght@400;500;600;700&family=Rajdhani:wght@700&display=swap" rel="stylesheet">
<style>
:root{
  --green:#a1c96a;
  --green-dark:#4e6b2c;
  --green-soft:#c9dfb0;
  --ink:#111;
  --dark:#232323;
  --darker:#1b1b1b;
  --grey:#8a8a8a;
  --light:#f8f8f6;
  --line:#e6e6e6;
  --white:#fff;
}
*{margin:0;padding:0;box-sizing:border-box}
html,body{width:1200px;height:2872px;overflow:hidden}
body{position:relative;font-family:Arial,Helvetica,sans-serif;color:var(--ink);background:var(--white)}
.abs{position:absolute}
.hd{font-family:'Montserrat',sans-serif}
.hl{color:var(--green)}
.btn{position:absolute;background:var(--green);color:var(--white);border-radius:24px;font-family:'Montserrat',sans-serif;font-weight:500;text-align:center;text-transform:uppercase}

/* top bar */
.topbar{left:0;top:0;width:1200px;height:38px;background:var(--green)}
.topbar .phone{left:766px;top:0;height:38px;line-height:38px;color:var(--white);font-size:14px;padding-left:26px}
.topbar .sep{top:0;width:1px;height:38px;background:rgba(255,255,255,.45)}
.topbar .soc{top:13px;width:12px;height:12px;border-radius:50%;background:rgba(255,255,255,.85)}

/* header */
.brand{left:162px;top:15px;width:82px;height:84px;background:var(--dark);border:4px solid var(--white);box-shadow:0 0 0 1px var(--line);color:var(--green);font-family:'Montserrat',sans-serif;font-weight:700;font-size:14px;line-height:18px;text-align:center;padding-top:19px}
.nav{top:67px;font-family:'Montserrat',sans-serif;font-size:11px;color:var(--grey)}
.nav.active{color:var(--ink)}
.nav-underline{left:505px;top:108px;width:30px;height:3px;background:var(--green)}
.search{left:814px;top:60px;width:224px;height:29px;border:1px solid var(--line);border-radius:15px;font-size:11px;font-style:italic;color:#999;padding:8px 12px}

/* hero */
.hero{left:0;top:113px;width:1200px;height:599px;background:var(--darker)}
.hero-title{left:164px;top:278px;font-family:'Rajdhani',sans-serif;font-weight:700;font-size:44px;line-height:49px;color:var(--white);letter-spacing:.5px}
.hero-text{left:163px;top:437px;width:380px;font-size:11px;line-height:19px;color:#e8e8e8}
.hero-circle{left:664px;top:226px;width:374px;height:374px;border-radius:50%;background:var(--green)}
.hero-doors{left:582px;top:262px;width:366px;height:300px;background:linear-gradient(180deg,#8a7468 0 8%,#d9dbdd 8%,#a9adb1 100%)}

/* sections */
.sec-title{left:0;width:1200px;text-align:center;font-family:'Montserrat',sans-serif;font-weight:600;font-size:33px;color:var(--ink)}
.sec-text{left:0;width:1200px;text-align:center;font-size:10.5px;line-height:19px;color:var(--grey)}
.svc-photo{left:162px;top:900px;width:314px;height:314px;background:linear-gradient(90deg,#cfd2d4,#f2f4f6 50%,#b9bdc0)}
.svc-icon{width:68px;height:68px;border-radius:50%;background:var(--green-soft);display:flex;align-items:center;justify-content:center}
.svc-icon.on{background:var(--green-dark)}
.svc-h{left:721px;font-family:'Montserrat',sans-serif;font-weight:600;font-size:16px}
.svc-p{left:721px;width:320px;font-size:10.5px;line-height:19px;color:var(--grey)}

.products{left:0;top:1273px;width:1200px;height:496px;background:var(--light)}
.card{top:1403px;width:202px;height:305px;background:var(--white);box-shadow:0 0 6px rgba(0,0,0,.05)}
.card .photo{position:absolute;left:7px;top:7px;width:188px;height:134px}
.card h3{position:absolute;top:162px;width:100%;text-align:center;font-family:'Montserrat',sans-serif;font-weight:500;font-size:13px}
.card p{position:absolute;top:188px;left:14px;width:174px;text-align:center;font-size:10.5px;line-height:17px;color:var(--grey)}
.card .btn{left:52px;top:252px;width:98px;height:28px;line-height:28px;font-size:10px}

.request{left:0;top:1769px;width:1200px;height:151px;background:var(--dark)}
.request h2{position:absolute;left:163px;top:38px;font-family:'Montserrat',sans-serif;font-weight:600;font-size:22px;color:var(--white)}
.request p{position:absolute;left:163px;top:76px;font-size:10.5px;line-height:19px;color:#e0e0e0}

.partner{top:2042px;width:134px;height:60px;border:1px solid #eee;display:flex;align-items:center;justify-content:center;font-family:'Montserrat',sans-serif;font-weight:700;font-size:13px;color:#333}

.contact-left{left:0;top:2167px;width:413px;height:390px;background:var(--green)}
.contact-right{left:413px;top:2167px;width:787px;height:390px;background:var(--dark)}
.map{left:162px;top:2234px;width:389px;height:263px;background:linear-gradient(135deg,#ecebe4,#dfe3d6)}
.field{left:622px;width:337px;border:1px solid #cfcfcf;border-radius:6px;background:#111;color:#eee;font-size:10.5px;padding:12px 9px}

.foot-h{top:2616px;font-family:'Montserrat',sans-serif;font-weight:600;font-size:14px}
.foot-li{font-size:10.5px;color:var(--grey)}
.foot-li b{color:#333}
.bottom{left:0;top:2796px;width:1200px;height:76px;background:var(--darker)}
.bottom p{position:absolute;left:163px;top:34px;font-size:10.5px;color:#ddd}
.bottom .c{position:absolute;top:16px;width:36px;height:36px;border-radius:50%;background:var(--green)}
</style>
</head>
<body>

<!-- top bar -->
<div class="abs topbar">
  <div class="abs phone">
    <svg class="abs" style="left:0;top:10px" width="18" height="18" viewBox="0 0 24 24"><path d="M6.6 10.8a15 15 0 0 0 6.6 6.6l2.2-2.2c.3-.3.7-.4 1-.2 1.1.4 2.3.6 3.6.6.6 0 1 .4 1 1V20c0 .6-.4 1-1 1A17 17 0 0 1 3 4c0-.6.4-1 1-1h3.5c.6 0 1 .4 1 1 0 1.3.2 2.5.6 3.6.1.3 0 .7-.2 1z" fill="#fff"/></svg>
    123.456.7890
  </div>
  <div class="abs sep" style="left:746px"></div>
  <div class="abs sep" style="left:888px"></div>
  <div class="abs sep" style="left:925px"></div>
  <div class="abs sep" style="left:962px"></div>
  <div class="abs sep" style="left:1000px"></div>
  <div class="abs soc" role="img" aria-label="Social link" style="left:901px"></div>
  <div class="abs soc" role="img" aria-label="Social link" style="left:938px"></div>
  <div class="abs soc" role="img" aria-label="Social link" style="left:975px"></div>
  <div class="abs soc" role="img" aria-label="Social link" style="left:1013px"></div>
</div>

<!-- header -->
<div class="abs brand">BAY &amp;<br>GATE</div>
<div class="abs nav active" style="left:504px">HOME</div>
<div class="abs nav" style="left:571px">PRODUCT</div>
<div class="abs nav" style="left:653px">SERVICES</div>
<div class="abs nav" style="left:736px">CONTACT</div>
<div class="abs nav-underline"></div>
<div class="abs search">Search here....
  <svg class="abs" style="right:12px;top:8px" width="13" height="13" viewBox="0 0 14 14"><circle cx="6" cy="6" r="4.5" fill="none" stroke="#222" stroke-width="1.5"/><path d="M9.3 9.3 13 13" stroke="#222" stroke-width="1.5"/></svg>
</div>

<!-- hero -->
<section class="abs hero"></section>
<div class="abs hero-circle"></div>
<div class="abs hero-doors" role="img" aria-label="Two roll-up industrial doors"></div>
<h1 class="abs hero-title"><span class="hl">DOCK</span> EQUIPMENT<br>AND <span class="hl">INDUSTRIAL</span><br>DOORS</h1>
<p class="abs hero-text">Lorem ipsum dolor sit amet, consectetur adipiscing elit, sed do eiusmod tempor incididunt ut labore et dolore magna aliqua. Ut enim ad minim veniam, quis nostrud exercitation ullamco laboris nisi ut aliquip.</p>
<div class="btn" style="left:162px;top:514px;width:112px;height:44px;line-height:44px;font-size:13px">Buy Now</div>

<!-- services -->
<h2 class="abs sec-title" style="top:768px">OUR <span class="hl">SERVICES</span></h2>
<p class="abs sec-text" style="top:829px">Lorem ipsum dolor sit amet, consectetur adipiscing elit, sed do eiusmod tempor incididunt<br>ut labore et dolore magna aliqua. Ut enim ad minim veniam, quis nostrud.</p>
<div class="abs svc-photo" role="img" aria-label="Stainless steel sliding door with window"></div>
<svg class="abs" style="left:476px;top:900px" width="200" height="320"><path d="M80 37 A130 130 0 0 1 80 277" fill="none" stroke="#eee" stroke-width="1.5"/></svg>
<div class="abs svc-icon" style="left:523px;top:903px">
  <svg width="34" height="34" viewBox="0 0 34 34" fill="none" stroke="#333" stroke-width="1.5"><rect x="9" y="4" width="16" height="27"/><rect x="13" y="9" width="8" height="9"/><path d="M4 31h26M20 21v3"/></svg>
</div>
<div class="abs svc-icon on" style="left:606px;top:1023px">
  <svg width="34" height="34" viewBox="0 0 34 34" fill="none" stroke="#fff" stroke-width="1.5"><path d="M10 4v6a3 3 0 0 0 6 0V4M13 13v17M20 10h10v20H20z"/><circle cx="25" cy="25" r="2"/></svg>
</div>
<div class="abs svc-icon" style="left:523px;top:1143px">
  <svg width="34" height="34" viewBox="0 0 34 34" fill="none" stroke="#333" stroke-width="1.5"><rect x="4" y="10" width="26" height="18" rx="2"/><path d="M13 10V6h8v4M10 19h14"/><circle cx="12" cy="19" r="2"/><circle cx="22" cy="19" r="2"/></svg>
</div>
<h3 class="abs svc-h" style="top:907px">INSTALLATION</h3>
<p class="abs svc-p" style="top:935px">Lorem ipsum dolor sit amet, consectetur adipiscing elit, sed does nisi ut aliquip ex ea commodo consequat.</p>
<h3 class="abs svc-h" style="top:1027px">REPAIR</h3>
<p class="abs svc-p" style="top:1055px">Lorem ipsum dolor sit amet, consectetur adipiscing elit, sed does nisi ut aliquip ex ea commodo consequat.</p>
<h3 class="abs svc-h" style="top:1140px">MAINTENANCE</h3>
<p class="abs svc-p" style="top:1167px">Lorem ipsum dolor sit amet, consectetur adipiscing elit, sed does nisi ut aliquip ex ea commodo consequat.</p>

<!-- products -->
<section class="abs products"></section>
<h2 class="abs sec-title" style="top:1323px">OUR <span class="hl">PRODUCTS</span></h2>
<div class="abs card" style="left:162px"><div class="photo" role="img" aria-label="Loading bay with dock levelers" style="background:linear-gradient(180deg,#c9401e,#2a6fb8 45%,#d7d5cf)"></div><h3>DOCK LEVELERS</h3><p>Lorem ipsum dolor sit amet, consectetur adipiscing elit, sed do dolore magna aliqua.</p><div class="btn">Read More</div></div>
<div class="abs card" style="left:387px"><div class="photo" role="img" aria-label="Row of dock seal panels" style="background:linear-gradient(180deg,#c8c7c6,#6b6663 50%,#e5e1dc)"></div><h3>DOCK PANELS</h3><p>Lorem ipsum dolor sit amet, consectetur adipiscing elit, sed do dolore magna aliqua.</p><div class="btn">Read More</div></div>
<div class="abs card" style="left:611px"><div class="photo" role="img" aria-label="Sectional dock door" style="background:linear-gradient(180deg,#8b8f95,#e8eaec 50%,#9aa0a6)"></div><h3>DOCK DOORS</h3><p>Lorem ipsum dolor sit amet, consectetur adipiscing elit, sed do dolore magna aliqua.</p><div class="btn">Read More</div></div>
<div class="abs card" style="left:836px"><div class="photo" role="img" aria-label="Warehouse with red roll-up door" style="background:linear-gradient(90deg,#b9bcbe,#c6403a 50%,#b3b6b8)"></div><h3>DOCK SHELTERS</h3><p>Lorem ipsum dolor sit amet, consectetur adipiscing elit, sed do dolore magna aliqua.</p><div class="btn">Read More</div></div>

<!-- service request -->
<section class="abs request">
  <h2>SUBMIT A <span class="hl">SERVICE REQUEST</span></h2>
  <p>Lorem ipsum dolor sit amet, consectetur adipiscing elit, sed do eiusmod tempor incididunt ut labore et dolore magna aliqua.<br>Ut enim ad minim veniam, quis nostrud.</p>
</section>
<div class="btn" style="left:903px;top:1822px;width:135px;height:44px;line-height:44px;font-size:13px">Contact Us</div>

<!-- partners -->
<h2 class="abs sec-title" style="top:1985px;font-size:19px">OUR PARTNERS</h2>
<div class="abs" style="left:162px;top:2007px;width:876px;height:1px;background:#eee"></div>
<div class="abs partner" style="left:167px">Pallan</div>
<div class="abs partner" style="left:313px">Garvin Holtby</div>
<div class="abs partner" style="left:459px">Pelma</div>
<div class="abs partner" style="left:605px">Morrow</div>
<div class="abs partner" style="left:751px">NHL Supplies</div>
<div class="abs partner" style="left:897px">VQX Gates</div>

<!-- contact -->
<div class="abs contact-left"></div>
<div class="abs contact-right"></div>
<div class="abs map" role="img" aria-label="Street map showing office location"></div>
<h2 class="abs hd" style="left:624px;top:2230px;font-weight:600;font-size:35px;color:#fff">CONTACT <span class="hl">US</span></h2>
<div class="abs field" style="top:2287px;height:37px">Name :</div>
<div class="abs field" style="top:2332px;height:37px">Emial :</div>
<div class="abs field" style="top:2378px;height:74px">Message / Comments :</div>
<div class="btn" style="left:622px;top:2460px;width:120px;height:37px;line-height:37px;font-size:13px">Submit Now</div>

<!-- footer -->
<div class="abs brand" style="left:222px;top:2616px;width:82px;height:91px;padding-top:23px;box-shadow:none">BAY &amp;<br>GATE</div>
<h4 class="abs foot-h" style="left:387px">OUR <span class="hl">SERVICES</span></h4>
<div class="abs foot-li" style="left:387px;top:2655px;line-height:22.5px">- &nbsp;Installation<br>- &nbsp;Repair<br>- &nbsp;Maintenance</div>
<h4 class="abs foot-h" style="left:574px">QUICK <span class="hl">LINKS</span></h4>
<div class="abs foot-li" style="left:574px;top:2655px;line-height:22.5px">- &nbsp;Home<br>- &nbsp;Products<br>- &nbsp;Services<br>- &nbsp;Contact</div>
<div class="abs foot-li" style="left:672px;top:2655px;line-height:22.5px">- &nbsp;Blog<br>- &nbsp;Testimonials<br>- &nbsp;Privacy Policy<br>- &nbsp;Terms &amp; Condition</div>
<h4 class="abs foot-h" style="left:837px">GET IN <span class="hl">TOUCH</span></h4>
<div class="abs foot-li" style="left:837px;top:2655px;line-height:19px">123,Address, State Nane, Street Name,<br>City Name, Zipcode</div>
<div class="abs foot-li" style="left:837px;top:2700px">Phone - <b>123.456.7890</b></div>
<div class="abs foot-li" style="left:837px;top:2730px">Email - <b>info@bayandgate.com</b></div>

<div class="abs bottom">
  <p>Copyright © BAY &amp; GATE NEW ENGLAND - 2020 . All Right Reserved.</p>
  <div class="c" role="img" aria-label="Social link" style="left:879px"></div>
  <div class="c" role="img" aria-label="Social link" style="left:920px"></div>
  <div class="c" role="img" aria-label="Social link" style="left:961px"></div>
  <div class="c" role="img" aria-label="Social link" style="left:1002px"></div>
</div>

</body>
</html>
```